Wordpress Web Design & Coding for velnoragroup.ca

We need a website for a new investment company that is visually grabbing and vibrant. We would like to see a web page that displays trust, growth and confidence. Needs to be responsive and mobile friendly for all browsers and coded for both Android & IOS.

Open to the number of pages and menu items. I selected 4 but if you feel the layout would work better with less I am open to this. Need to sell the people (management team/related businesses) and then show where the invested money will be going (upcoming projects).

Company Info:

Velnora is an investment company put together by a group of seasoned business professionals who have come together to combine decades of success in the real estate development, management, financing and medical services. The company will be a full service company offering turn key solutions for medical professionals.

Vel-Nora will focus on providing a full range of services via a group of distinct companies to deliver newly emerging needs of the medical community. The end goal will be to create complete solutions for individuals in the medical community. Our group has experience and success with the conceptualization, construction and financing of medical and dental clinic spaces. Vel-Nora Group will be established to accommodate all areas of the development and creation of clinics for medical professionals from building construction to equipment financing and administrations.

You can mention these companies and take photos from their websites. You can also use stock photos.

Our construction partner:
https://382bld.com/projects/

Our equipment leasing partner:
https://www.pordiva.com/

Our Management Team and medical partners

Gil Parkes
https://www.mysoundpoise.ca/

Milos Vendraker
https://www.qrtdentalservices.com/about-us

PROPOSED PROJECTS (see attachment for details)
Hollowmere Business Park
Cresfield Business Park
Mt. Corwin Ridge Professional

Investors

Investment

Sans Serif

Must have
• Wordpress – must be both desktop and mobile friendly with fast page load speed
Ability to edit after ourselves in Wordpress
Attractive home page with logo etc.
Logo colours are: for the blue the pantone color is #0355a3
and for the green is #8cc63f

Sections, about us, what we do/services we provide, contact us

```html
<!DOCTYPE html>
<html lang="en">
<head>
<meta charset="utf-8">
<title>Velnora – Canada's Fastest Growing Investment Company</title>
<link href="https://fonts.googleapis.com/css2?family=Poppins:wght@400;500;600;700;800&family=Open+Sans:wght@400;600;700&display=swap" rel="stylesheet">
<style>
:root{
  --blue:#0355a3;
  --green:#8cc63f;
  --navy:#0b1b5c;
  --navy-dark:#081346;
  --panel:#2a4ea2;
  --sky:#4fc3f7;
  --ink:#1d2a44;
  --muted:#6d7380;
  --light:#f3f5f8;
  --white:#ffffff;
}
*{box-sizing:border-box;margin:0;padding:0}
html,body{width:1200px;height:3676px;overflow:hidden}
body{font-family:"Open Sans",sans-serif;color:var(--ink);background:var(--white);position:relative}
h1,h2,h3,h4,.brand,.nav a,.btn{font-family:"Poppins",sans-serif}
.photo{position:absolute;display:block}

/* Hero */
.hero{position:absolute;left:0;top:0;width:1200px;height:540px;overflow:hidden}
.hero .photo{inset:0;background:linear-gradient(120deg,#3c4a50 0%,#5f6d70 35%,#2d3a40 70%,#1f2a30 100%)}
.hero .shade{position:absolute;inset:0;background:rgba(10,20,30,.45)}
.topbar{position:absolute;left:0;top:0;width:1200px;height:64px;background:rgba(255,255,255,.96);display:flex;align-items:center;justify-content:space-between;padding:0 60px}
.brand{display:flex;align-items:center;gap:10px;font-weight:700;font-size:22px;color:var(--blue)}
.brand i{width:26px;height:26px;border-radius:50%;background:var(--green);display:block}
.nav{display:flex;height:64px}
.nav a{display:flex;align-items:center;padding:0 18px;font-size:13px;font-weight:600;color:var(--ink);text-decoration:none;text-transform:uppercase}
.nav a.active{background:var(--navy);color:var(--white)}
.hero h1{position:absolute;left:0;top:100px;width:1200px;text-align:center;color:var(--white);font-size:60px;line-height:70px;font-weight:800}
.hero h1 span{color:var(--sky)}
.hero p{position:absolute;left:190px;top:330px;width:820px;color:var(--white);font-size:18px;line-height:26px}
.hero svg{position:absolute;left:0;bottom:0}

/* About */
.section-title{position:absolute;left:0;width:1200px;text-align:center;font-weight:700}
.about-title{top:560px;color:var(--green);font-size:40px}
.about-text{position:absolute;left:170px;width:860px;text-align:center;font-size:14px;line-height:22px;color:var(--muted)}
.partner{position:absolute;top:790px;width:424px;height:380px;background:var(--white);box-shadow:0 4px 18px rgba(0,0,0,.12)}
.partner .photo{left:0;top:0;width:424px;height:160px}
.partner h3{position:absolute;left:0;top:140px;background:var(--white);padding:12px 24px 6px 20px;font-size:20px;font-weight:700;color:var(--ink);white-space:nowrap}
.partner p{position:absolute;left:20px;top:196px;width:384px;font-size:12px;line-height:19px;color:var(--muted)}
.partner .mark{position:absolute;left:20px;top:318px;display:flex;align-items:center;gap:8px;font-family:"Poppins",sans-serif;font-weight:700;font-size:18px;color:var(--navy)}
.partner .mark i{width:20px;height:20px;background:var(--blue);display:block}
.partner .mark.right{left:auto;right:30px;color:var(--ink)}

/* Management */
.team{position:absolute;left:0;top:1170px;width:1200px;height:400px;background:linear-gradient(100deg,#d7ecc0 0%,var(--green) 45%,#7fbc36 70%,#b9dd8f 100%)}
.team h2{position:absolute;left:0;top:40px;width:1200px;text-align:center;font-size:36px;color:var(--navy);font-weight:700}
.member{position:absolute;top:130px;width:500px;height:220px}
.member .photo{left:0;top:20px;width:140px;height:140px;border-radius:50%;border:4px solid var(--white)}
.member h3{position:absolute;left:170px;top:0;font-size:30px;font-weight:700;color:var(--ink)}
.member p{position:absolute;left:170px;top:46px;width:310px;font-size:14px;line-height:20px;color:var(--navy);font-weight:600}
.member.alt h3{color:var(--white)}
.member.alt p{color:var(--white)}
.btn{position:absolute;display:inline-block;padding:9px 20px;font-size:13px;font-weight:600;color:var(--white);background:var(--navy);border-radius:3px;white-space:nowrap}
.member .btn{right:20px;top:178px}

/* Leasing & Security */
.panel{position:absolute;background:var(--panel);color:var(--white);padding:28px 32px}
.panel h2{font-size:30px;font-weight:700;margin-bottom:16px}
.panel p,.panel li{font-size:13px;line-height:20px;color:#e4eaf8}
.leasing{left:120px;top:1600px;width:580px;height:360px}
.leasing-photo{left:700px;top:1610px;width:400px;height:320px;background:linear-gradient(135deg,#d9cdbb,#8c7a63 60%,#4b4034)}
.security-photo{left:100px;top:1980px;width:470px;height:440px;background:radial-gradient(circle at 50% 45%,#5ab0ff 0%,#1e5ac8 40%,#0a1c55 100%)}
.security{left:560px;top:2020px;width:540px;height:400px;padding-top:24px}
.security-title{position:absolute;left:450px;top:1925px;font-family:"Poppins",sans-serif;font-size:36px;font-weight:700;color:var(--white);background:var(--panel);padding:6px 22px}
.security ul{list-style:none;margin-top:10px}
.security li{position:relative;padding-left:18px;margin-bottom:5px}
.security li:before{content:"";position:absolute;left:2px;top:8px;width:6px;height:6px;border-radius:50%;background:var(--green)}

/* Contracts */
.contracts{position:absolute;left:0;top:2460px;width:1200px;height:690px;background:linear-gradient(180deg,#ffffff 0%,#e8eef3 30%,#dbe3ea 100%)}
.contracts .photo{inset:0;background:linear-gradient(160deg,rgba(255,255,255,0) 0%,rgba(190,205,215,.55) 60%,rgba(150,170,185,.5) 100%)}
.contracts h2{position:absolute;left:160px;top:130px;font-size:40px;font-weight:700;color:var(--blue)}
.project{position:absolute;top:220px;width:270px;height:420px;background:var(--white);box-shadow:0 4px 16px rgba(0,0,0,.15)}
.project .photo{left:12px;top:12px;width:246px;height:160px}
.project h3{position:absolute;left:18px;top:186px;width:240px;font-size:17px;font-weight:700;color:var(--ink);line-height:22px}
.project p{position:absolute;left:18px;top:216px;width:236px;font-size:12px;line-height:18px;color:var(--muted)}
.project .btn{left:50%;transform:translateX(-50%);top:364px;background:var(--green)}

/* Footer */
.footer{position:absolute;left:0;top:3150px;width:1200px;height:440px;background:var(--navy)}
.footer h4{font-size:20px;font-weight:600;color:var(--white);margin-bottom:18px}
.footer .col{position:absolute;top:50px}
.footer ul{list-style:none}
.footer li{font-size:14px;color:#c7cff0;margin-bottom:10px;display:flex;align-items:center;gap:12px}
.footer li b{width:7px;height:7px;background:var(--green);border-radius:50%;display:block}
.footer svg{flex:none}
.copyright{position:absolute;left:0;top:3590px;width:1200px;height:86px;background:var(--navy-dark);color:#aab4dd;font-size:13px;display:flex;align-items:center;justify-content:center}
</style>
</head>
<body>

<header class="hero">
  <div class="photo" role="img" aria-label="Dentist at work in a modern clinic, darkened backdrop"></div>
  <div class="shade"></div>
  <div class="topbar">
    <div class="brand"><i></i>Velnora</div>
    <nav class="nav">
      <a class="active">Home</a><a>About Us</a><a>Service We Provide</a><a>Contact Us</a>
    </nav>
  </div>
  <h1>Canada's<br><span>Fastest Growing Investment</span><br>Company!</h1>
  <p>Velnora is an investment company put together by a group of seasoned business professionals who have come together to combine decades of success in the real estate development, management, financing and medical services.</p>
  <svg width="1200" height="80" viewBox="0 0 1200 80"><path d="M0 40 C300 80 600 0 900 30 C1040 45 1130 40 1200 20 L1200 80 L0 80 Z" fill="#ffffff"/></svg>
</header>

<h2 class="section-title about-title">About Us</h2>
<p class="about-text" style="top:630px">We are a group of seasoned business professionals who have come together to combine decades of success in the real estate development, management, financing and medical services. This initial foundation of experience and the strong network of relationships built along the way will be developed to support the growing needs of the medical community.</p>
<p class="about-text" style="top:720px">As an initiative of the venture, complete clinic solutions will follow, from construction and equipment financing through to administration of healthcare spaces across Canada.</p>

<article class="partner" style="left:160px">
  <div class="photo" role="img" aria-label="Modern commercial building under a blue sky" style="background:linear-gradient(180deg,#7fb6e6 0%,#bcd6ec 55%,#8a96a3 100%)"></div>
  <h3>Construction Partner</h3>
  <p>Our construction partner has delivered medical and dental clinic spaces across western Canada, handling design, permits and building from the ground up with a focus on quality, schedule and budget for every client project.</p>
  <div class="mark"><i></i>382 Developments Inc.</div>
</article>

<article class="partner" style="left:616px">
  <div class="photo" role="img" aria-label="Bright dental treatment room with equipment" style="background:linear-gradient(180deg,#eef3f6 0%,#cfdbe3 60%,#9fb3c0 100%)"></div>
  <h3>Equipment Leasing Partner</h3>
  <p>Our equipment leasing partner provides flexible financing for medical and dental equipment, helping professionals open and grow their practices with tailored terms, fast approvals and dependable long term support.</p>
  <div class="mark right">Pordiva Equipment Leasing</div>
</article>

<section class="team">
  <h2>Our Management Team and medical partners</h2>
  <div class="member" style="left:80px">
    <div class="photo" role="img" aria-label="Portrait of Dr. Gil Parkes" style="background:linear-gradient(160deg,#c9d3dc,#7c8a96)"></div>
    <h3>Dr. Gil Parkes</h3>
    <p>A published author and experienced, board certified physician in the field of regenerative medicine, Dr. Parkes brings years of clinical leadership and a proven track record in practice growth.</p>
    <a class="btn">Read More</a>
  </div>
  <div class="member alt" style="left:640px">
    <div class="photo" role="img" aria-label="Portrait of Milos Vendraker" style="background:linear-gradient(160deg,#b7c6d2,#5f7080)"></div>
    <h3>Milos Vendraker</h3>
    <p>Milos brings over 20 years of experience in partnering with dental groups across western Canada as a clinic consultant, having built and managed successful practices.</p>
    <a class="btn">Read More</a>
  </div>
</section>

<section class="panel leasing">
  <h2>Leasing Operations</h2>
  <p>The Vel-Nora Group leasing division will secure long term tenancies with established medical and dental professionals across western Canada. The leasing model will allow investors to take advantage of a leverage portfolio and earn a stable return on the investment with the security of commercial real estate assets. A structured repayment of interest and principal will be invested in the participants. As the funds grow, the investment base will expand to include new clinics and medical facilities. Management will work to build on existing relationships with tenants, lenders and partners so each project is completed with a strong position for revenue and distribution.</p>
</section>
<div class="photo leasing-photo" role="img" aria-label="Modern office interior with meeting table"></div>

<div class="photo security-photo" role="img" aria-label="Digital padlock illustration symbolising investment security"></div>
<section class="panel security">
  <p>The Vel-Nora Group leasing division will implement a number of security measures which ensure investors are secure and returns are protected over the life of the agreement:</p>
  <ul>
    <li>All leases will be tied to the assets with funds flowing to investors.</li>
    <li>The lease agreement will be established with companies that are operating revenue generating clinics.</li>
    <li>The lease agreement is registered against the property title.</li>
    <li>Leases are signed by the owners of the practice and are personally guaranteed.</li>
    <li>The leased portfolio is insured for full replacement value.</li>
    <li>Payments collected monthly are deposited into a trust account.</li>
    <li>Average outstanding lease amounts will be less than 80% of value.</li>
  </ul>
</section>
<div class="security-title">Security</div>

<section class="contracts">
  <div class="photo" role="img" aria-label="Faded skyline of commercial buildings"></div>
  <h2>Contracts...</h2>
  <article class="project" style="left:132px">
    <div class="photo" role="img" aria-label="Rendering of a modern business park building" style="background:linear-gradient(180deg,#cfe0ee,#8d9aa6)"></div>
    <h3>Cresfield Business Park</h3>
    <p>Planning of the development is under way and located in a growing community on the west coast. It is currently experiencing rapid growth in population with a mix of residential and commercial space.</p>
    <a class="btn">Read More</a>
  </article>
  <article class="project" style="left:465px">
    <div class="photo" role="img" aria-label="Rendering of a professional office building" style="background:linear-gradient(180deg,#d8e4ee,#9aa7b2)"></div>
    <h3>Mt. Corwin Ridge Professional</h3>
    <p style="top:238px">The professional building will feature a purpose built medical space of about 14,000 square feet with room for clinics and related services serving the area.</p>
    <a class="btn">Read More</a>
  </article>
  <article class="project" style="left:798px">
    <div class="photo" role="img" aria-label="Rendering of a business park with parking" style="background:linear-gradient(180deg,#dde8f0,#a3aeb8)"></div>
    <h3>Hollowmere Business Park</h3>
    <p>The business park is located in a growing suburban community with a strong demand for medical services, with plans for a mix of clinics and offices.</p>
    <a class="btn">Read More</a>
  </article>
</section>

<footer class="footer">
  <div class="col" style="left:170px">
    <h4>Useful Links</h4>
    <ul>
      <li><b></b>Home</li>
      <li><b></b>About us</li>
      <li><b></b>Services we provide</li>
      <li><b></b>Contact us</li>
      <li><b></b>Our Partners</li>
      <li><b></b>Contracts</li>
    </ul>
  </div>
  <div class="col" style="left:600px">
    <h4>Contact Information</h4>
    <ul>
      <li><svg width="16" height="20" viewBox="0 0 16 20"><path d="M8 0C3.6 0 0 3.5 0 7.8 0 13.6 8 20 8 20s8-6.4 8-12.2C16 3.5 12.4 0 8 0zm0 11a3.2 3.2 0 110-6.4A3.2 3.2 0 018 11z" fill="#8cc63f"/></svg>Lorem ipsum dolor sit amet, consectetur adipiscing elit</li>
      <li><svg width="18" height="18" viewBox="0 0 18 18"><path d="M4 1l3 4-2 2c1 2 3 4 5 5l2-2 4 3-2 4C7 16 2 11 1 4z" fill="#8cc63f"/></svg><strong style="color:#fff">+1 000 0000 00</strong></li>
      <li><svg width="18" height="14" viewBox="0 0 18 14"><rect x="0.5" y="0.5" width="17" height="13" rx="1" fill="none" stroke="#8cc63f"/><path d="M1 1l8 7 8-7" fill="none" stroke="#8cc63f"/></svg>Email: info@velnoragroup.ca</li>
    </ul>
  </div>
</footer>
<div class="copyright">Copyright © All rights reserved. Theme Illustrated by Northpine Theme</div>

</body>
</html>
```